Packaging Graphics Design for TR electronics device

We need a designer to design the graphics that will be printed to the packaging we have designed for our Tenvo Ridge electronics device. Our device is significantly larger but the packacking concept is similar to that of a mobile phone and we envisage the graphics being similar to those used by the main brand. We provide the following additional information:
1. Power point presentation with a more detailed briefing
2. Various renders of our Tenvo Ridge electronics device
3. Packaging design with all components and corresponding dimensions
4. Tenvo Labs logo

```html
<!DOCTYPE html>
<html lang="en">
<head>
<meta charset="utf-8">
<title>Tenvo Ridge packaging dieline</title>
<link rel="stylesheet" href="https://fonts.googleapis.com/css2?family=Montserrat:wght@300;400;800&family=Roboto:wght@400&display=swap">
<style>
  :root {
    --stage: #575757;
    --measure: #ffffff;
    --panel-light: #fafafa;
    --panel-mid: #ececec;
    --panel-edge: #1a1a1a;
    --ink: #111111;
    --rule: #8a8a8a;
    --device-shell: #f2f4f6;
    --device-screen: #0a0a0a;
  }
  html, body { margin: 0; padding: 0; overflow: hidden; }
  body { width: 1200px; height: 986px; background: var(--stage); position: relative; font-family: "Montserrat", sans-serif; }

  .measure-lines { position: absolute; left: 0; top: 0; }
  .measure-label { position: absolute; color: var(--measure); font-family: "Roboto", sans-serif; font-size: 33px; line-height: 1; white-space: nowrap; }
  .measure-label.horizontal { top: 84px; transform: translateX(-50%); }
  .measure-label.vertical { left: 1110px; transform: translate(-50%, -50%) rotate(90deg); }

  .panel { position: absolute; border: 1px solid var(--panel-edge); box-sizing: border-box;
    background: linear-gradient(135deg, var(--panel-light) 0%, var(--panel-mid) 30%, var(--panel-light) 50%, var(--panel-mid) 75%, var(--panel-light) 100%); overflow: hidden; }
  .panel.lid-top { left: 312px; top: 163px; width: 485px; height: 218px; }
  .panel.lid-bottom { left: 312px; top: 651px; width: 485px; height: 218px; }
  .panel.side-left { left: 95px; top: 380px; width: 218px; height: 272px; }
  .panel.face { left: 312px; top: 380px; width: 485px; height: 272px; }
  .panel.side-right { left: 796px; top: 380px; width: 218px; height: 272px; }

  .product-title { position: absolute; color: var(--ink); font-size: 23px; font-weight: 300; letter-spacing: 1px; white-space: nowrap; line-height: 1; }
  .product-title strong { font-weight: 800; }
  .product-title .title-rule { display: block; width: 46px; height: 1px; background: var(--rule); margin: 0 auto 12px; }
  .lid-top .product-title, .lid-bottom .product-title { left: 50%; top: 58px; transform: translateX(-50%) rotate(180deg); text-align: center; }
  .face .product-title { font-size: 17px; left: 44px; top: 136px; transform: translate(-50%, -50%) rotate(90deg); text-align: center; }
  .face .product-title .title-rule { width: 18px; margin-bottom: 8px; }

  .device-render { position: absolute; left: 85px; top: 39px; width: 313px; height: 194px; border-radius: 14px 40px 40px 14px;
    background: linear-gradient(90deg, var(--device-shell) 0%, var(--device-shell) 38%, var(--device-screen) 40%, #1c1c1c 85%, var(--device-shell) 90%); box-shadow: 0 2px 4px rgba(0,0,0,.25); }

  .maker-mark { position: absolute; display: flex; align-items: center; gap: 10px; color: var(--ink); white-space: nowrap; line-height: 1; }
  .maker-mark .mark-square { width: 30px; height: 30px; background: var(--ink); flex: none; }
  .maker-mark .mark-name { font-size: 18px; font-weight: 800; letter-spacing: 3px; }
  .side-left .maker-mark { left: 109px; top: 136px; transform: translate(-50%, -50%) rotate(90deg); }
  .face .maker-mark { left: 442px; top: 126px; transform: translate(-50%, -50%) rotate(90deg); }
  .side-right .maker-mark { left: 107px; top: 126px; transform: translate(-50%, -50%) rotate(-90deg); }
</style>
</head>
<body>
  <svg class="measure-lines" width="1200" height="986" aria-hidden="true">
    <g stroke="#ffffff" stroke-width="1" fill="none">
      <line x1="95" y1="74" x2="1013" y2="74"/>
      <line x1="95" y1="64" x2="95" y2="85"/>
      <line x1="312" y1="74" x2="312" y2="85"/>
      <line x1="796" y1="74" x2="796" y2="85"/>
      <line x1="1013" y1="64" x2="1013" y2="85"/>
      <line x1="1130" y1="163" x2="1130" y2="868"/>
      <line x1="1119" y1="163" x2="1140" y2="163"/>
      <line x1="1119" y1="380" x2="1130" y2="380"/>
      <line x1="1119" y1="652" x2="1130" y2="652"/>
      <line x1="1119" y1="868" x2="1140" y2="868"/>
    </g>
  </svg>

  <div class="measure-label horizontal" style="left:227px">80mm</div>
  <div class="measure-label horizontal" style="left:571px">228mm</div>
  <div class="measure-label horizontal" style="left:872px">80mm</div>
  <div class="measure-label vertical" style="top:253px">80mm</div>
  <div class="measure-label vertical" style="top:514px">128mm</div>
  <div class="measure-label vertical" style="top:762px">80mm</div>

  <section class="panel lid-top">
    <div class="product-title"><span class="title-rule"></span>TENVO <strong>RIDGE</strong></div>
  </section>

  <section class="panel side-left">
    <div class="maker-mark"><span class="mark-square"></span><span class="mark-name">TENVO LABS</span></div>
  </section>

  <section class="panel face">
    <div class="product-title"><span class="title-rule"></span>TENVO <strong>RIDGE</strong></div>
    <div class="device-render" role="img" aria-label="Product render of the Tenvo Ridge device: white shell with a large black screen, seen from above"></div>
    <div class="maker-mark"><span class="mark-square"></span><span class="mark-name">TENVO LABS</span></div>
  </section>

  <section class="panel side-right">
    <div class="maker-mark"><span class="mark-square"></span><span class="mark-name">TENVO LABS</span></div>
  </section>

  <section class="panel lid-bottom">
    <div class="product-title"><span class="title-rule"></span>TENVO <strong>RIDGE</strong></div>
  </section>
</body>
</html>
```